Resume/CV/Cover Letter templates

We are a career management business and are starting to offer tailored career documents. we want 3-4 styles/themes with resume and cover letter templates. I have some examples to show you that are a good starting point (but are someone else's IP). see attached files

Target Market(s)

Corporate

Font styles to use
Sans Serif

Requirements
Must have
• Clean lines. Simple formatting. Corporate look and feel. Not too busy.
• Matching resume and cover letter documents
Nice to have
• One Blue theme
• One Green theme
• One other
Should not have
• too much jazziness!

```html
<!DOCTYPE html>
<html lang="en">
<head>
<meta charset="utf-8">
<title>Green Theme – Cover Letter &amp; CV Templates</title>
<link rel="stylesheet" href="https://fonts.googleapis.com/css2?family=Varela+Round&family=Roboto+Condensed:wght@700&family=Source+Sans+3:ital,wght@0,400;0,600;0,700;1,600&family=Tinos:ital@1&display=swap">
<style>
:root{
  --board:#4d4d4d;
  --paper:#ffffff;
  --green:#8a9b27;
  --green-text:#7f9420;
  --ink:#1f1f1f;
  --band:#262626;
  --rule:#8a9b27;
  --letter-blue:#3b5c9a;
}
*{box-sizing:border-box;margin:0;padding:0}
html,body{width:1200px;height:1200px;overflow:hidden;background:var(--board)}
body{position:relative;font-family:"Source Sans 3",Arial,sans-serif;color:var(--ink)}
.board-title{position:absolute;left:0;width:1200px;text-align:center;font-family:"Varela Round",sans-serif;font-weight:400;color:#fff;letter-spacing:2px}
.board-title.cover{top:54px;font-size:33px}
.board-title.cv{top:618px;font-size:28px;letter-spacing:3px}

.page{position:absolute;background:var(--paper);box-shadow:6px 8px 14px rgba(0,0,0,.45);overflow:hidden}
.abs{position:absolute;white-space:nowrap}
.stripe{position:absolute;left:0;top:0;bottom:0;background:var(--green)}

/* cover letter */
.letter{left:432px;top:110px;width:338px;height:473px}
.letter .stripe{width:21px}
.letter-head{position:absolute;left:21px;top:0;right:0;height:54px;background:var(--band)}
.letter-name{left:29px;top:9px;font-family:"Roboto Condensed",sans-serif;font-weight:700;font-size:28px;color:var(--green-text);letter-spacing:-.3px}
.contact{left:29px;top:40px;font-size:5px;color:#fff;font-weight:600;display:flex;gap:8px;align-items:center}
.contact span{display:flex;align-items:center;gap:2px}
.contact svg{width:5px;height:5px;fill:var(--green)}
.letter-date{left:29px;top:57px;font-size:7px;color:var(--green-text)}
.small{font-size:5px;font-weight:600}
.letter-re{left:29px;top:99px;font-size:7.5px;color:var(--green-text);font-weight:600}
.letter-rule{position:absolute;left:29px;top:111px;width:294px;height:1px;background:var(--rule)}
.criteria{position:absolute;left:29px;top:116px;width:221px;height:133px;border-top:2px solid #dfe7ee;border-bottom:1px solid #dfe7ee}
.criteria-title{position:absolute;left:24px;top:3px;font-family:"Tinos",serif;font-style:italic;font-size:6.5px;color:var(--letter-blue)}
.criteria-caret{position:absolute;right:6px;top:3px;font-size:5px;color:var(--letter-blue)}
.criteria ul{position:absolute;left:32px;top:30px;width:180px;list-style:none;font-size:4.6px;line-height:7px;color:#444}
.criteria li{position:relative;margin-bottom:2px}
.criteria li::before{content:"";position:absolute;left:-7px;top:2.5px;width:2px;height:2px;border-radius:50%;background:#b7c400}
.letter-body{position:absolute;left:29px;top:255px;width:296px;font-size:5px;line-height:6.6px}
.letter-body p{margin-bottom:3.5px}
.ticks{list-style:none}
.ticks li{position:relative;padding-left:11px;margin-bottom:2.5px}
.ticks svg{position:absolute;left:0;top:1px;width:7px;height:6px}
.ticks b{color:var(--green-text);font-weight:600;font-size:5.4px}
.sign{color:var(--green-text);font-style:italic;font-weight:600;font-size:5.6px}

/* CV pages */
.cv-page{top:683px;width:300px;height:421px}
.cv-one{left:70px}
.cv-two{left:451px}
.cv-three{left:830px}
.cv-two .stripe,.cv-three .stripe{width:23px}
.sidebar{position:absolute;left:0;top:0;width:98px;height:100%;background:var(--green);color:#fff;text-align:center}
.cv-head{position:absolute;left:98px;top:0;right:0;height:33px;background:var(--band)}
.cv-name{left:102px;top:12px;font-family:"Roboto Condensed",sans-serif;font-weight:700;font-size:15px;color:var(--green-text)}
.photo{position:absolute;left:16px;top:11px;width:72px;height:72px;border-radius:50%;border:2px solid #2a2a2a;background:radial-gradient(circle at 50% 40%,#e9ddd2,#b9b2ad 70%,#8e8a88)}
.side-icon{position:absolute;left:43px;width:12px;height:12px}
.side-text{position:absolute;left:6px;width:86px;font-size:5px;line-height:7px}
.side-bold{font-weight:700;font-size:5.4px}
.skills-title{position:absolute;left:12px;top:247px;font-family:"Varela Round",sans-serif;font-size:11px;letter-spacing:1.5px}
.skills{position:absolute;left:12px;top:264px;width:80px;text-align:left;list-style:none;font-size:4.8px;line-height:7px}
.skills li{margin-bottom:5px;text-align:justify}

.sec{position:absolute;font-family:"Varela Round",sans-serif;font-weight:400;color:var(--green-text);font-size:9px;letter-spacing:.8px;display:flex;align-items:center;gap:6px;white-space:nowrap}
.sec::after{content:"";display:block;height:1px;background:var(--rule);flex:1}
.cv-one .sec{left:117px;right:13px}
.cv-two .sec{left:33px;right:13px}
.cv-three .sec{left:34px;right:13px}
.sub{position:absolute;font-family:"Varela Round",sans-serif;font-weight:400;color:var(--green-text);font-size:8.5px;letter-spacing:.4px;white-space:nowrap;-webkit-text-stroke:.25px var(--green-text)}
.para{position:absolute;font-size:5px;line-height:7px;text-align:justify}
.item{position:absolute;font-size:5px;white-space:nowrap}
.item::before{content:"• ";color:var(--green)}
.proj{position:absolute;font-size:5px;white-space:nowrap}
.proj b{color:var(--green-text);font-size:7.5px;font-weight:600}
.jobrow{position:absolute;font-size:5px;font-weight:700;white-space:nowrap}
.summary{position:absolute;left:117px;top:125px;width:180px;border-collapse:separate;border-spacing:2px 0;font-size:4.8px}
.summary th{background:var(--green);color:#fff;text-align:left;padding:1px 2px;font-weight:700;height:9px}
.summary td{height:14.7px;padding-left:2px;vertical-align:middle}
.edu{position:absolute;left:117px;font-size:4.8px;white-space:nowrap}
.edu span:last-child{position:absolute;left:77px}
</style>
</head>
<body>

<h1 class="board-title cover">Cover Letter</h1>

<article class="page letter">
  <div class="stripe"></div>
  <header class="letter-head"></header>
  <div class="abs letter-name">DANIELMARSH</div>
  <div class="abs contact">
    <span><svg viewBox="0 0 10 10"><path d="M5 0a3.5 3.5 0 0 0-3.5 3.5C1.5 6 5 10 5 10s3.5-4 3.5-6.5A3.5 3.5 0 0 0 5 0z"/></svg>12 Harbour Lane, Eastfield, NSW 2600</span>
    <span><svg viewBox="0 0 10 10"><path d="M2 0l2 2.5-1 1.5a6 6 0 0 0 3 3l1.5-1L10 8l-1.5 2C4 10 0 6 0 1.5z"/></svg>0400 123 456</span>
    <span><svg viewBox="0 0 10 10"><rect x="0" y="2" width="10" height="6"/></svg>d.marsh@mailbox.example</span>
  </div>
  <div class="abs letter-date">8 November 2017</div>
  <div class="abs small" style="left:29px;top:72px">Attention: Laura Bennett</div>
  <div class="abs small" style="left:29px;top:79px">Hillside College</div>
  <div class="abs small" style="left:29px;top:91px;font-weight:400">Dear Laura</div>
  <div class="abs letter-re">RE: Religious Education Teacher</div>
  <div class="letter-rule"></div>

  <section class="criteria">
    <div class="criteria-title">Essential criteria for teaching positions</div>
    <div class="criteria-caret">^</div>
    <ul>
      <li>Possess a deep understanding and commitment to the mission and purpose of an all-girl College embracing its founding values and its long-held tradition.</li>
      <li>Strong knowledge of curriculum including appropriate teaching qualifications and accreditation.</li>
      <li>An ability and interest in the integration of ICT to supplement and support education in the classroom.</li>
      <li>Well-developed interpersonal skills with the ability to work collaboratively in a team environment.</li>
      <li>Knowledge of the holistic approach to education which challenges the creativity, initiative and ability of each student.</li>
      <li>Willingness to operate within the Pastoral Care framework of the College.</li>
    </ul>
  </section>

  <div class="letter-body">
    <p>I write to apply for the Administrator role within your Finance Department and I attach my CV as evidence of my suitability for this position.</p>
    <p>I am excited by this opportunity to join a dynamic and growing organisation within the health and wellness industry and, in accordance with your requirements, I offer the following skills and attributes:</p>
    <ul class="ticks">
      <li><svg viewBox="0 0 10 8"><path d="M1 4l3 3 5-6" fill="none" stroke="#7f9420" stroke-width="1.8"/></svg><b>Strong Administration Background:</b> I have 20 years of experience within business administration, customer service and finance roles and proven success in driving quality and efficiency and administration and reporting activity and delivering continuous improvement in financial performance through effective credit control and debt recovery.</li>
      <li><svg viewBox="0 0 10 8"><path d="M1 4l3 3 5-6" fill="none" stroke="#7f9420" stroke-width="1.8"/></svg><b>Excellent Numerical Skills with High Attention to Detail:</b> Working within the Insurance and Financial Services sectors I have worked with a range of databases and software systems, managing customer data with the highest standards of accuracy and ensuring the integrity and timeliness of payment transactions.</li>
      <li><svg viewBox="0 0 10 8"><path d="M1 4l3 3 5-6" fill="none" stroke="#7f9420" stroke-width="1.8"/></svg><b>IT Literate:</b> I have worked extensively with spreadsheet software and the wider office software suite and have demonstrated aptitude for learning new IT systems with ease, having adapted to the implementation of new finance and customer relationship management (CRM) systems within various organisations.</li>
      <li><svg viewBox="0 0 10 8"><path d="M1 4l3 3 5-6" fill="none" stroke="#7f9420" stroke-width="1.8"/></svg><b>Exemplary Communication, Customer Service &amp; Relationship Management:</b> Working in call centre environments and fast-paced service-focused roles, with B2B and B2C clients, I have demonstrated exemplary communication skills to establish rapport, trust and credibility with internal and external customers; resolving disputes and negotiating repayments and settlements.</li>
      <li><svg viewBox="0 0 10 8"><path d="M1 4l3 3 5-6" fill="none" stroke="#7f9420" stroke-width="1.8"/></svg><b>Organisation &amp; Planning:</b> I have strong time management and prioritisation skills, working closely with colleagues to monitor and manage workflow effectively across the team.</li>
    </ul>
    <p>I thank you in advance for your consideration of my application and I welcome the opportunity to demonstrate the value I can bring to your team.</p>
    <p>Yours sincerely,</p>
    <p class="sign">Sarah Lowe</p>
  </div>
</article>

<h2 class="board-title cv">CV</h2>

<article class="page cv-page cv-one">
  <aside class="sidebar">
    <div class="photo" role="img" aria-label="Portrait photo of the candidate"></div>
    <svg class="side-icon" style="top:96px" viewBox="0 0 12 12"><circle cx="6" cy="6" r="6" fill="#fff"/><path d="M6 2.5a2.2 2.2 0 0 0-2.2 2.2C3.8 6.4 6 9.5 6 9.5s2.2-3.1 2.2-4.8A2.2 2.2 0 0 0 6 2.5z" fill="#2a2a2a"/></svg>
    <div class="side-text" style="top:111px">Lorem ipsum, or lipsum as it is sometimes known, is dummy text used in laying out print.</div>
    <svg class="side-icon" style="top:143px" viewBox="0 0 12 12"><circle cx="6" cy="6" r="6" fill="#fff"/><path d="M4 2.8l1.2 1.6-.6.9a3.6 3.6 0 0 0 1.9 1.9l.9-.6L9 7.8l-.9 1.2C5.4 9 3 6.6 3 3.7z" fill="#2a2a2a"/></svg>
    <div class="side-text side-bold" style="top:158px;line-height:7px">123-456-789<br>123-456-789</div>
    <svg class="side-icon" style="top:180px" viewBox="0 0 12 12"><circle cx="6" cy="6" r="6" fill="#fff"/><rect x="3" y="4" width="6" height="4" fill="#2a2a2a"/></svg>
    <div class="side-text" style="top:195px">anna@mailbox.example</div>
    <svg class="side-icon" style="top:207px" viewBox="0 0 12 12"><circle cx="6" cy="6" r="6" fill="#fff"/><circle cx="6" cy="6" r="3" fill="none" stroke="#2a2a2a" stroke-width="1"/><path d="M3 6h6M6 3v6" stroke="#2a2a2a" stroke-width=".7"/></svg>
    <div class="side-text" style="top:222px">Lorem ipsum, or lipsum as it is sometimes</div>
    <div class="skills-title">KEY SKILLS</div>
    <ul class="skills">
      <li class="side-bold" style="font-size:4.8px">• [SKILL] – [DESCRIPTION]</li>
      <li>• <b>Commercial Acumen</b> – applies sound commercial knowledge to deliver robust market analysis; accurately identifying risk and opportunity to inform strategic planning and to enable effective negotiation, management and review of contracts</li>
      <li>• <b>[Skill]</b> – [Description]</li>
      <li>• <b>[Skill]</b> – [Description]</li>
      <li>• <b>[Skill]</b> – [Description]</li>
      <li>• <b>[Skill]</b> – [Description]</li>
      <li>• <b>[Skill]</b> – [Description]</li>
    </ul>
  </aside>
  <header class="cv-head"></header>
  <div class="abs cv-name">ANNAKOVALSKA</div>

  <h3 class="sec" style="top:39px">CAREER PROFILE</h3>
  <p class="para" style="left:117px;top:51px;width:171px;line-height:6.9px">Lorem ipsum dolor sit amet, consectetur adipiscing elit, sed do eiusmod tempor incididunt ut labore et dolore magna aliqua. Ut enim ad minim veniam, quis nostrud exercitation ullamco laboris nisi ut aliquip ex ea commodo consequat. Duis aute irure dolor in reprehenderit in voluptate velit esse cillum dolore eu fugiat nulla pariatur. Excepteur sint occaecat cupidatat non proident, sunt in culpa qui officia deserunt mollit anim id est laborum.</p>

  <h3 class="sec" style="top:108px">CAREER SUMMARY</h3>
  <table class="summary">
    <tr><th>DATES</th><th>POSITION</th><th>ORGANISATION</th></tr>
    <tr><td>[Date] to [Date]</td><td>[Position]</td><td>[Organisation]</td></tr>
    <tr><td>[Date] to [Date]</td><td>[Position]</td><td>[Organisation]</td></tr>
    <tr><td>[Date] to [Date]</td><td>[Position]</td><td>[Organisation]</td></tr>
    <tr><td>[Date] to [Date]</td><td>[Position]</td><td>[Organisation]</td></tr>
    <tr><td>[Date] to [Date]</td><td>[Position]</td><td>[Organisation]</td></tr>
    <tr><td>[Date] to [Date]</td><td>[Position]</td><td>[Organisation]</td></tr>
  </table>

  <h3 class="sec" style="top:231px">EDUCATION</h3>
  <div class="edu" style="top:246px"><span>[Year]</span><span>[Course name, Institution]</span></div>
  <div class="edu" style="top:260px"><span>[Year]</span><span>[Course name, Institution]</span></div>
  <div class="edu" style="top:275px"><span>[Year]</span><span>[Course name, Institution]</span></div>

  <h3 class="sec" style="top:293px">COMPUTER / TECHNICAL SKILLS</h3>
  <div class="item" style="left:117px;top:307px">[Insert text]</div>
  <div class="item" style="left:117px;top:320px">[Insert text]</div>
  <div class="item" style="left:117px;top:333px">[Insert text]</div>
  <div class="item" style="left:117px;top:345px">[Insert text]</div>
  <div class="item" style="left:117px;top:358px">[Insert text]</div>

  <h3 class="sec" style="top:373px">AWARDS / ACHIEVEMENTS</h3>
  <div class="item" style="left:117px;top:387px">[Insert text]</div>
  <div class="item" style="left:117px;top:399px">[Insert text]</div>
</article>

<article class="page cv-page cv-two">
  <div class="stripe"></div>
  <h3 class="sec" style="top:10px">EMPLOYMENT HISTORY</h3>
  <div class="jobrow" style="left:33px;top:29px">[Job title],</div>
  <div class="jobrow" style="left:114px;top:29px">[Company name]</div>
  <div class="jobrow" style="left:215px;top:29px">[Job dates]</div>
  <p class="para" style="left:33px;top:46px;width:255px">Lorem ipsum dolor sit amet, consectetur adipiscing elit, sed do eiusmod tempor incididunt ut labore et dolore magna aliqua. Ut enim ad minim veniam, quis nostrud exercitation ullamco laboris nisi ut aliquip ex ea commodo consequat. Lorem ipsum dolor sit amet, consectetur adipiscing elit, sed do eiusmod tempor incididunt ut labore et dolore magna aliqua. Ut enim ad minim veniam, quis nostrud exercitation ullamco laboris nisi ut aliquip ex ea commodo consequat. Duis aute irure dolor in reprehenderit in voluptate velit esse cillum dolore eu fugiat nulla pariatur. Excepteur sint occaecat cupidatat non proident, sunt in culpa qui officia deserunt mollit anim id est laborum.</p>
  <div class="sub" style="left:33px;top:101px">RESPONSIBILITIES</div>
  <div class="item" style="left:33px;top:114px">[Insert text]</div>
  <div class="sub" style="left:33px;top:134px">ACHIEVEMENTS</div>
  <div class="item" style="left:33px;top:148px">[Insert text]</div>
  <div class="sub" style="left:33px;top:169px">KEY PROJECTS</div>
  <div class="proj" style="left:33px;top:185px"><b>Project:</b>[Insert text]</div>
  <div class="proj" style="left:33px;top:199px"><b>Role/Focus:</b>[Insert text]</div>
  <div class="proj" style="left:33px;top:213px"><b>Project:</b>[Insert text]</div>
  <div class="proj" style="left:33px;top:228px"><b>Role/Focus:</b>[Insert text]</div>
  <div class="jobrow" style="left:33px;top:245px">[Job title],</div>
  <div class="jobrow" style="left:114px;top:245px">[Company name]</div>
  <div class="jobrow" style="left:216px;top:245px">[Job dates]</div>
  <p class="para" style="left:33px;top:259px;width:255px">Lorem ipsum dolor sit amet, consectetur adipiscing elit, sed do eiusmod tempor incididunt ut labore et dolore magna aliqua. Ut enim ad minim veniam, quis nostrud exercitation ullamco laboris nisi ut aliquip ex ea commodo consequat. Lorem ipsum dolor sit amet,</p>
  <div class="sub" style="left:33px;top:304px">RESPONSIBILITIES</div>
  <div class="item" style="left:33px;top:317px">[Insert text]</div>
  <div class="sub" style="left:33px;top:349px">ACHIEVEMENTS</div>
  <div class="item" style="left:33px;top:362px">[Insert text]</div>
</article>

<article class="page cv-page cv-three">
  <div class="stripe"></div>
  <div class="sub" style="left:34px;top:10px">KEY PROJECTS</div>
  <div class="proj" style="left:34px;top:33px"><b>Project:</b>[Insert text]</div>
  <div class="proj" style="left:34px;top:48px"><b>Role/Focus:</b>[Insert text]</div>
  <div class="proj" style="left:34px;top:63px"><b>Project:</b>[Insert text]</div>
  <div class="proj" style="left:34px;top:77px"><b>Role/Focus:</b>[Insert text]</div>
  <div class="jobrow" style="left:34px;top:94px">[Job title],</div>
  <div class="jobrow" style="left:116px;top:94px">[Company name]</div>
  <div class="jobrow" style="left:218px;top:94px">[Job dates]</div>
  <p class="para" style="left:34px;top:107px;width:255px">Lorem ipsum dolor sit amet, consectetur adipiscing elit, sed do eiusmod tempor incididunt ut labore et dolore magna aliqua. Ut enim ad minim veniam, quis nostrud exercitation ullamco laboris nisi ut aliquip ex ea commodo consequat. Lorem ipsum dolor sit amet,</p>
  <div class="sub" style="left:34px;top:137px">RESPONSIBILITIES</div>
  <div class="item" style="left:34px;top:151px">[Insert text]</div>
  <div class="sub" style="left:34px;top:167px">ACHIEVEMENTS</div>
  <div class="item" style="left:34px;top:180px">[Insert text]</div>
  <div class="sub" style="left:34px;top:198px">KEY PROJECTS</div>
  <div class="proj" style="left:34px;top:221px"><b>Project:</b>[Insert text]</div>
  <div class="proj" style="left:34px;top:236px"><b>Role/Focus:</b>[Insert text]</div>
  <div class="proj" style="left:34px;top:250px"><b>Project:</b>[Insert text]</div>
  <div class="proj" style="left:34px;top:265px"><b>Role/Focus:</b>[Insert text]</div>
  <h3 class="sec" style="top:286px">PROFESSIONAL MEMBERSHIPS</h3>
  <div class="item" style="left:34px;top:303px">[Insert text]</div>
  <div class="item" style="left:34px;top:316px">[Insert text]</div>
  <h3 class="sec" style="top:333px">REFERENCES</h3>
  <div class="item" style="left:34px;top:354px">[Insert text]</div>
</article>

</body>
</html>
```